Stationary for decorative plumbing and hardware showroom
Fine Home Fittings
Professional
Wendell Okafor
2417 Morrow Parkway
Suite 420
Houston, TX 77091
wendell@lumivessa.com
www.lumivessa.com

```html
<!DOCTYPE html>
<html lang="en">
<head>
<meta charset="utf-8">
<title>LumiVessa — Business Cards</title>
<link href="https://fonts.googleapis.com/css2?family=Raleway:wght@300;400;600&display=swap" rel="stylesheet">
<style>
  :root {
    --canvas: #dedede;
    --card: #ffffff;
    --ink: #2a2a2a;
    --text: #555555;
    --silver: #9a9a9a;
    --band-grey: #b9b9b9;
    --band-black: #1c1c1c;
  }
  * { margin: 0; padding: 0; box-sizing: border-box; }
  html, body { width: 1200px; height: 984px; overflow: hidden; }
  body {
    background: var(--canvas);
    font-family: "Raleway", sans-serif;
    display: flex;
    flex-direction: column;
    align-items: center;
    justify-content: center;
    gap: 40px;
  }
  .card {
    position: relative;
    width: 760px;
    height: 434px;
    background: var(--card);
    border-radius: 18px;
    overflow: hidden;
    box-shadow: 0 2px 6px rgba(0,0,0,0.08);
  }
  .brand-name {
    position: absolute;
    left: 0; right: 0;
    text-align: center;
    font-weight: 300;
    letter-spacing: 2px;
    line-height: 1;
  }

  /* Card back */
  .card-back .brand-name { top: 140px; font-size: 84px; color: var(--silver); }
  .card-back .web {
    position: absolute; bottom: 80px; left: 0; right: 0;
    text-align: center; font-size: 17px; letter-spacing: 8px; color: var(--silver);
  }

  /* Card front */
  .card-front .brand-name { top: 50px; font-size: 58px; color: var(--ink); }
  .card-front .person {
    position: absolute; top: 146px; left: 0; right: 0;
    text-align: center; font-size: 17px; font-weight: 600; color: var(--ink);
  }
  .card-front .address {
    position: absolute; top: 194px; left: 130px;
    font-size: 14px; font-style: normal; line-height: 1.55; color: var(--text);
  }
  .card-front .contacts {
    position: absolute; top: 186px; left: 420px;
    list-style: none; font-size: 14px; color: var(--text);
  }
  .contacts li { display: flex; align-items: center; gap: 9px; height: 22px; }
  .contacts svg { width: 15px; height: 15px; flex: none; }
  .waves { position: absolute; left: 0; bottom: 0; width: 760px; height: 434px; }
</style>
</head>
<body>

  <section class="card card-back">
    <div class="brand-name">LumiVessa</div>
    <div class="web">www.lumivessa.com</div>
  </section>

  <section class="card card-front">
    <svg class="waves" viewBox="0 0 760 434" aria-hidden="true">
      <path d="M0,300 C210,285 330,395 760,362 L760,434 L0,434 Z" fill="var(--band-grey)"/>
      <path d="M0,318 C215,304 330,410 760,382 L760,434 L0,434 Z" fill="#ffffff"/>
      <path d="M0,330 C220,318 330,420 760,398 L760,434 L0,434 Z" fill="var(--band-black)"/>
    </svg>
    <div class="brand-name">LumiVessa</div>
    <div class="person">Wendell Okafor</div>
    <address class="address">
      2417 Morrow Parkway Suite 420<br>
      Houston, TX 77091
    </address>
    <ul class="contacts">
      <li>
        <svg viewBox="0 0 16 16"><circle cx="8" cy="8" r="8" fill="var(--ink)"/><path d="M5.2 4.2l1.6 1.6-0.9 1.2c0.6 1.2 1.5 2.1 2.7 2.7l1.2-0.9 1.6 1.6-1.2 1.3c-2.8-0.6-5-2.8-5.6-5.6z" fill="#fff"/></svg>
        713-555-0148
      </li>
      <li>
        <svg viewBox="0 0 16 16"><circle cx="8" cy="8" r="8" fill="var(--ink)"/><rect x="5.5" y="3.5" width="5" height="9" rx="1" fill="#fff"/><rect x="6.5" y="4.8" width="3" height="5.2" fill="var(--ink)"/></svg>
        832-555-0162
      </li>
      <li>
        <svg viewBox="0 0 16 16"><circle cx="8" cy="8" r="8" fill="var(--ink)"/><rect x="4" y="6.5" width="8" height="5" rx="1" fill="#fff"/><rect x="5.5" y="4" width="5" height="3" fill="#fff"/></svg>
        713-555-0193
      </li>
      <li>
        <svg viewBox="0 0 16 16"><circle cx="8" cy="8" r="8" fill="var(--ink)"/><rect x="4" y="5" width="8" height="6" fill="#fff"/><path d="M4 5l4 3.3L12 5" fill="none" stroke="var(--ink)" stroke-width="0.9"/></svg>
        wendell@lumivessa.com
      </li>
      <li>
        <svg viewBox="0 0 16 16"><circle cx="8" cy="8" r="8" fill="var(--ink)"/><circle cx="8" cy="8" r="4" fill="none" stroke="#fff" stroke-width="0.9"/><ellipse cx="8" cy="8" rx="1.8" ry="4" fill="none" stroke="#fff" stroke-width="0.9"/><path d="M4 8h8" stroke="#fff" stroke-width="0.9"/></svg>
        www.lumivessa.com
      </li>
    </ul>
  </section>

</body>
</html>
```